Interior Design & consultancy firm requires a new business card design that is a little bit funky bu

Meridale Design Services is a leading strategic design practice specialising in the development and implementation of strategies and design solutions for commercial workplaces across a wide variety of industries.

The company has over twenty years experience in the strategic design, development and construction of innovative and efficient workplace environments for the commercial, corporate and industrial sectors.

We believe good design and efficient workspaces can transform companies, improve people’s lives and increase productivity.

Target Market(s)

My clients are mainly Government or corporate clients wanting to create a statement with their office fitout & new furniture that reflects their corporate identity

Industry/Entity Type

Construction

Font styles to use
Sans Serif

Colors
add136

Requirements
Must have
• The business card must be easy to read, simple & highlight my name & mobile phone number
Should not have
• I do not want the card to be fussy, feature too many colours or look to busy.

```html
<!DOCTYPE html>
<html lang="en">
<head>
<meta charset="utf-8">
<title>Meridale Design Services – Business Card</title>
<link rel="stylesheet" href="https://fonts.googleapis.com/css2?family=Open+Sans:wght@400;600&family=Roboto+Condensed:wght@700&display=swap">
<style>
  :root {
    --lime: #add136;
    --dark: #2c3b3b;
    --paper: #f7f8f6;
    --ink: #4a4f4f;
    --backdrop: #e9e7e3;
  }
  * { margin: 0; padding: 0; box-sizing: border-box; }
  html, body { width: 1200px; height: 900px; overflow: hidden; }
  body { background: var(--backdrop); position: relative; }

  .card {
    position: absolute;
    left: 250px;
    width: 700px;
    height: 400px;
    background: var(--paper);
    box-shadow: 0 6px 18px rgba(0,0,0,.18);
    overflow: hidden;
  }
  .card--back { top: 40px; }
  .card--front { top: 470px; }

  .card__band { position: absolute; left: 0; top: 0; width: 700px; height: 400px; }

  .brand-mark {
    position: absolute;
    left: 190px;
    top: 90px;
    display: flex;
    align-items: center;
    gap: 14px;
    font-family: "Open Sans", sans-serif;
    font-weight: 600;
    font-size: 40px;
    color: var(--lime);
  }
  .brand-mark__dot { width: 26px; height: 26px; border-radius: 50%; background: var(--lime); }

  .company-name {
    position: absolute;
    left: 0; right: 0;
    top: 318px;
    display: flex;
    align-items: center;
    gap: 18px;
    padding: 0 30px;
    font-family: "Roboto Condensed", sans-serif;
    font-weight: 700;
    font-size: 38px;
    letter-spacing: 1px;
    text-transform: uppercase;
    color: var(--lime);
    white-space: nowrap;
  }
  .rule { flex: 1; height: 3px; background: var(--lime); }

  .person { position: absolute; left: 110px; top: 92px; width: 500px; }
  .person__name {
    font-family: "Open Sans", sans-serif;
    font-weight: 400;
    font-size: 52px;
    line-height: 1;
    letter-spacing: 1px;
    text-transform: uppercase;
    color: var(--lime);
    padding-bottom: 8px;
    border-bottom: 2px solid var(--ink);
  }
  .person__title {
    margin-top: 8px;
    padding-left: 30px;
    font-family: "Open Sans", sans-serif;
    font-size: 19px;
    letter-spacing: .5px;
    text-transform: uppercase;
    color: var(--ink);
  }

  .phone {
    position: absolute;
    left: 0; right: 0;
    top: 318px;
    display: flex;
    align-items: center;
    gap: 22px;
    padding: 0 30px;
    font-family: "Roboto Condensed", sans-serif;
    font-weight: 700;
    font-size: 48px;
    letter-spacing: 2px;
    color: var(--lime);
    white-space: nowrap;
  }
</style>
</head>
<body>
  <section class="card card--back">
    <svg class="card__band" viewBox="0 0 700 400" aria-hidden="true">
      <path d="M0 290 C 200 285, 450 230, 700 150 L700 400 L0 400 Z" fill="var(--dark)"/>
      <path d="M0 290 C 200 285, 450 230, 700 150" fill="none" stroke="var(--lime)" stroke-width="4"/>
    </svg>
    <div class="brand-mark"><span class="brand-mark__dot"></span>Meridale</div>
    <div class="company-name"><span class="rule"></span>Meridale Design Services<span class="rule"></span></div>
  </section>

  <section class="card card--front">
    <svg class="card__band" viewBox="0 0 700 400" aria-hidden="true">
      <path d="M0 250 C 250 270, 450 290, 700 280 L700 400 L0 400 Z" fill="var(--dark)"/>
      <path d="M0 250 C 250 270, 450 290, 700 280" fill="none" stroke="var(--lime)" stroke-width="4"/>
    </svg>
    <div class="person">
      <h1 class="person__name">Karen Whitfield</h1>
      <p class="person__title">Director &amp; Senior Interior Designer</p>
    </div>
    <div class="phone"><span class="rule"></span>0412 555 018<span class="rule"></span></div>
  </section>
</body>
</html>
```